Political sign design, fonts colors and layout

I am running for Town Council.

My message is done, and *a draft is attached* with the text we wish to use. It says "Elect Dana Velloway" etc. In Maroon and White. I am not a designer, but this is somewhat close to what we are looking for.

I need help with colors and fonts, layout, spacing, and general cleanup.

I'm attaching the town high school logo:

- "B" for Brockmere: with black and white outlines on the fonts
- we want to incorporate the black and white on the fonts
- for the entire text, parts of the text, or best would be a mix

This is for signs printed and placed all over my town.

We need two versions

1. square, 4' by 4' version
2. 36" by 24" version

The smaller version will drop the three bullet pointed text, but otherwise can be identical.

The sign can only use 3 printed colors (due to printing costs.)

1. maroon,
2. white,
3. black.

The maroon should match the maroon from the high school logo attached, which I believe I did in the draft.

We also like the white border around the outside, like in the "scoreboard" design attached.

Thanks for your attention, wish me luck.

Dana

Target Market(s)

SIgns, Political market

Industry/Entity Type

Political

Font styles to use
Sans Serif
Other font styles liked:
• Arial Black, Sans Serif Bold

Requirements
Must have
• maroon background, white font.
• - black borders around fonts where appropriate
• - great spacing
• - great typeface usage
• - clean and crisp political sign, visible while driving.
• - my name "Dana Velloway" much larger like the draft, or the appropriate additional size
• - two versions, one square, and one 36" / 24"
Nice to have
• - nice borders
• - dress it up a bit, using italics and bold fonts, without making it flashy or busy.
Should not have
• Must be easily readable from a car, except for "Paid for by Friends of Dana Velloway" which can be tiny.
• Colors are noted in the description, the "Brockmere Maroon" as the background, white font, and some use of black.

```html
<!DOCTYPE html>
<html lang="en">
<head>
<meta charset="utf-8">
<title>Elect Dana Velloway – Yard Sign</title>
<link rel="stylesheet" href="https://fonts.googleapis.com/css2?family=Arimo:wght@700&family=Raleway:wght@700;800;900&display=swap">
<style>
  :root {
    --maroon: #731030;
    --white: #ffffff;
    --black: #000000;
  }
  html, body {
    margin: 0;
    padding: 0;
    width: 1200px;
    height: 1200px;
    overflow: hidden;
    background: var(--black);
  }
  .yard-sign {
    position: absolute;
    left: 100px;
    top: 100px;
    width: 1000px;
    height: 1000px;
    display: block;
  }
  .sign-face { fill: var(--white); }
  .maroon-fill { fill: var(--maroon); }
  .slogan, .rally-line, .vote-line {
    font-family: "Raleway", sans-serif;
    font-weight: 900;
    fill: var(--maroon);
  }
  .website {
    font-family: "Raleway", sans-serif;
    font-weight: 800;
    fill: var(--maroon);
  }
  .elect-label, .office-line, .platform-item {
    font-family: "Raleway", sans-serif;
    font-weight: 800;
    fill: var(--white);
    stroke: var(--black);
    stroke-width: 1.2;
    paint-order: stroke;
  }
  .platform-item { font-weight: 700; }
  .candidate-name {
    font-family: "Arimo", sans-serif;
    font-weight: 700;
    fill: var(--white);
    stroke: var(--black);
    stroke-width: 5;
    paint-order: stroke;
    stroke-linejoin: round;
  }
  .disclaimer {
    font-family: "Raleway", sans-serif;
    font-weight: 700;
    fill: var(--white);
  }
  .checkbox-frame { fill: var(--white); stroke: var(--black); stroke-width: 3; }
  .checkmark { fill: var(--maroon); }
</style>
</head>
<body>
<svg class="yard-sign" viewBox="0 0 875 875" role="img" aria-label="Elect Dana Velloway for Brockmere Councilman / Trustee campaign sign">
  <rect class="sign-face" x="0" y="0" width="875" height="875"/>
  <rect class="maroon-fill top-band" x="0" y="0" width="875" height="17"/>

  <text class="slogan" x="437.5" y="97" text-anchor="middle" font-size="72" textLength="818" lengthAdjust="spacingAndGlyphs">TAKE BACK OUR TOWN!</text>

  <g class="name-panel">
    <rect class="maroon-fill" x="14" y="127" width="847" height="355"/>
    <text class="elect-label" x="37" y="270" font-size="45">Elect</text>
    <rect class="checkbox-frame" x="39" y="286" width="126" height="125"/>
    <path class="checkmark" d="M50 352 L70 338 L100 375 L152 300 L160 308 L103 403 Z"/>
    <text class="candidate-name" x="198" y="276" font-size="162">DANA</text>
    <text class="candidate-name" x="198" y="412" font-size="132" textLength="632" lengthAdjust="spacingAndGlyphs">VELLOWAY</text>
    <text class="office-line" x="200" y="459" font-size="33" textLength="630" lengthAdjust="spacingAndGlyphs">for Brockmere Councilman / Trustee</text>
  </g>

  <text class="rally-line" x="437.5" y="556" text-anchor="middle" font-size="68" textLength="790" lengthAdjust="spacingAndGlyphs">FIGHTING for BROCKMERE</text>
  <text class="website" x="437.5" y="586" text-anchor="middle" font-size="25">www.vellowayforcouncil.com</text>

  <g class="platform-panel">
    <rect class="maroon-fill" x="14" y="600" width="847" height="163"/>
    <text class="platform-item" x="437.5" y="648" text-anchor="middle" font-size="33">STOP HIGH TAXES</text>
    <text class="platform-item" x="437.5" y="696" text-anchor="middle" font-size="33">CLEAN UP OUR GOVERNMENT</text>
    <text class="platform-item" x="437.5" y="743" text-anchor="middle" font-size="33">PRESERVE OUR NEIGHBORHOODS</text>
  </g>

  <text class="vote-line" x="437.5" y="836" text-anchor="middle" font-size="66">Vote Nov 8<tspan font-size="38" dy="-26">th</tspan><tspan dy="26"> “Row A”</tspan></text>

  <rect class="maroon-fill bottom-band" x="0" y="848" width="875" height="27"/>
  <text class="disclaimer" x="853" y="868" text-anchor="end" font-size="13">Paid for by Friends of Dana Velloway</text>
</svg>
</body>
</html>
```